Mobile Landing Page for giveaway Seedbombs done from a institution for handicaped people

We are a social institution that makes seedbombs that contain wildflowers for bees and other insects. During a sutanibel event, these bombs are given to an audience. On the packaging of the seedbombs, there is a QR code that leads to a landing page. We are producing a video showing how our handicapped clients made the seebombs. The Landigpage should look: sustanible, green, and sozial. On the page, there shoud be this Video, a manual how tho use the seedbombs. Something about our work whith the handicapt people a linkt to our Instagram amd a possibility to get involved whith us as well as a donation button. You can find more information about us on: www.brenzelgut.ch

Target Market(s)

People that are intressetet in envirement and social impakt

Industry/Entity Type

Social Impakt, Urban Gardening

Coding

Coded - Design and coding required

Number of Pages Required

1 page

Other font styles liked:
• Joanna

Requirements
Must have
• Be optimised for smartphone
Nice to have
• like a floating page, witch leads you throug the different steps, mabey like a plant with ist growing. From the Bombs to the Plan. Or a little game ore something.

```html
<!DOCTYPE html>
<html lang="en">
<head>
<meta charset="utf-8">
<title>Brenzelgut – Seedbombs</title>
<link href="https://fonts.googleapis.com/css2?family=Trirong:wght@400;500;600&family=Jost:wght@400;500&display=swap" rel="stylesheet">
<style>
:root{
  --forest:#233f33;
  --forest-deep:#1d362b;
  --sage:#b3c0a4;
  --sage-light:#c5cfb8;
  --blush:#f6e3dc;
  --paper:#f2f0ec;
  --terracotta:#c9604b;
  --ink:#22392e;
  --cream:#eef0e6;
  --serif:"Trirong", Georgia, serif;
  --sans:"Jost", Arial, sans-serif;
}
*{margin:0;padding:0;box-sizing:border-box}
html,body{width:1200px;height:2961px;overflow:hidden}
body{background:var(--paper);position:relative;font-family:var(--sans);color:var(--ink)}
.top-band{position:absolute;left:0;top:0;width:1200px;height:497px;background:var(--sage)}
.brand-title{position:absolute;left:264px;top:56px;font-family:var(--serif);font-size:52px;font-weight:500;letter-spacing:3px;color:var(--forest)}
.page{position:absolute;overflow:hidden;background:var(--forest)}
.desk{left:159px;top:175px;width:546px;height:1451px}
.mobile{left:875px;top:175px;width:176px;height:2656px}
.abs{position:absolute}
.band{position:absolute;left:0;width:100%}
.hero{background:var(--forest);top:0}
.sage{background:var(--sage)}
.blush{background:var(--blush)}
.photo{position:absolute}
.ph-workshop{background:linear-gradient(135deg,#c9b79a,#8e7a62 55%,#3d4f6b)}
.ph-box{background:linear-gradient(135deg,#e9ece6,#8fa98a 60%,#5e7c5c)}
.ph-tools{background:linear-gradient(135deg,#efe9e1,#b48a66 50%,#3e3429)}
.ph-field{background:linear-gradient(135deg,#7f8b5a,#a08d6e 55%,#5a4a3a)}
.ph-a{background:linear-gradient(135deg,#b94a3e,#d9b23a)}
.ph-b{background:linear-gradient(135deg,#6d5a45,#b0473b)}
.ph-c{background:linear-gradient(135deg,#3a3330,#9b8b7a)}
.ph-d{background:linear-gradient(135deg,#8fa2c2,#b45a32)}
.ph-e{background:linear-gradient(135deg,#d9dbe0,#5f8a3a)}
.ph-f{background:linear-gradient(135deg,#7a9a4a,#b45a3e)}
.ph-g{background:linear-gradient(135deg,#2f2a22,#9a7a3a)}
.ph-h{background:linear-gradient(135deg,#c8a684,#c0602e)}
.logo-text{font-family:var(--serif);font-weight:500;color:#fff;letter-spacing:1px;white-space:nowrap}
.badge{position:absolute;border-radius:50%;background:var(--terracotta)}
.eyebrow{font-size:5px;letter-spacing:.5px;text-transform:uppercase;color:#fff}
.h1{font-family:var(--serif);color:#fff;font-weight:400}
.body-light{color:#dfe6da;line-height:1.6}
.body-dark{color:var(--ink);line-height:1.6}
.center{text-align:center}
.btn{position:absolute;display:flex;align-items:center;justify-content:center;font-weight:500;white-space:nowrap}
.btn-sage{background:var(--sage);color:var(--forest)}
.btn-forest{background:var(--forest);color:#fff}
.btn-outline{border:1px solid var(--forest);color:var(--forest)}
.btn-outline-light{border:1px solid var(--forest);color:var(--forest);background:transparent}
.h2{font-family:var(--serif);color:var(--forest);font-weight:400;line-height:1.2}
.h2 b{font-weight:600}
.icon{position:absolute}
.label{font-family:var(--serif);color:var(--forest)}
.video-card{position:absolute;background:var(--forest)}
.video-title{font-family:var(--serif);color:var(--sage-light);line-height:1.15}
.video-title b{font-weight:600}
.newsletter{position:absolute;background:var(--sage)}
.footer-head{font-family:var(--serif);color:#dfe6da}
.footer-text{color:#dfe6da;line-height:1.55}
.social{position:absolute;border-radius:50%;background:#fff}
.rule{position:absolute;height:1px;background:rgba(255,255,255,.18)}
.input-line{position:absolute;height:1px;background:var(--forest)}
.placeholder{font-family:var(--serif);font-style:italic;color:#4d5f4f}
</style>
</head>
<body>

<div class="top-band"></div>
<div class="brand-title">BRENZELGUT</div>

<!-- Desktop layout -->
<section class="page desk" aria-label="Desktop landing page">
  <div class="band blush" style="top:640px;height:623px"></div>
  <div class="band sage" style="top:228px;height:572px;border-bottom-left-radius:62px"></div>
  <div class="band hero" style="height:228px"></div>

  <div class="abs logo-text" style="left:48px;top:12px;font-size:12px">BRENZELGUT</div>
  <div class="badge" style="left:455px;top:11px;width:42px;height:42px"></div>

  <div class="abs eyebrow" style="left:91px;top:72px">Welcome to</div>
  <div class="abs h1" style="left:91px;top:80px;font-size:21px">Brenzelgut</div>
  <p class="abs body-light" style="left:91px;top:126px;width:178px;font-size:6px">A differentiated range of day activities and an individually adapted care setting are aimed at adults of all ages with a mental disability and with physical and psychological impairments.</p>
  <div class="btn btn-sage" style="left:91px;top:180px;width:74px;height:16px;font-size:5px">Explore seedbombs →</div>

  <div class="photo ph-workshop" role="img" aria-label="Photo of two clients working on wooden crafts in the workshop" style="left:318px;top:43px;width:228px;height:185px;border-top-left-radius:44px;border-bottom-right-radius:32px"></div>
  <div class="photo ph-workshop" role="img" aria-label="Small workshop detail photo" style="left:318px;top:228px;width:43px;height:42px"></div>

  <div class="photo ph-box" role="img" aria-label="Photo of the green seedbomb package" style="left:0;top:263px;width:172px;height:153px"></div>
  <div class="abs" style="left:207px;top:287px;font-family:var(--serif);font-size:7px;color:var(--forest)">Love ♥ Gardening?</div>
  <div class="abs h2" style="left:207px;top:298px;font-size:17px;font-weight:600">Seedbombs kit</div>
  <p class="abs body-dark" style="left:207px;top:327px;width:130px;font-size:5.5px">A differentiated range of day activities and an individually adapted care setting are aimed at adults ...</p>
  <div class="abs" style="left:207px;top:366px;font-family:var(--serif);font-size:8px;color:var(--forest)">$199.00</div>
  <div class="btn btn-forest" style="left:207px;top:391px;width:74px;height:16px;font-size:5px">Explore seedbombs →</div>
  <div class="btn btn-outline" style="left:285px;top:391px;width:50px;height:16px;font-size:5px">Add to cart →</div>
  <div class="photo ph-tools" role="img" aria-label="Photo of seed trays, soil and garden tools" style="left:372px;top:325px;width:174px;height:142px;border-top-left-radius:40px"></div>

  <div class="abs h2 center" style="left:0;top:505px;width:546px;font-size:16px">Manual how to use the<br><b>seedbombs</b></div>

  <svg class="icon" style="left:109px;top:557px" width="46" height="46" viewBox="0 0 46 46" aria-hidden="true"><circle cx="23" cy="23" r="21" fill="none" stroke="#233f33" stroke-width="1"/><path d="M23 2 A21 21 0 0 1 44 23" fill="none" stroke="#233f33" stroke-width="2"/><circle cx="23" cy="21" r="4" fill="none" stroke="#233f33"/><path d="M15 30 Q23 26 31 30" fill="none" stroke="#233f33"/></svg>
  <svg class="icon" style="left:202px;top:557px" width="46" height="46" viewBox="0 0 46 46" aria-hidden="true"><circle cx="23" cy="23" r="21" fill="none" stroke="#233f33" stroke-width="1"/><path d="M23 2 A21 21 0 0 1 44 23" fill="none" stroke="#233f33" stroke-width="2"/><path d="M23 15 Q29 23 23 29 Q17 23 23 15Z" fill="none" stroke="#233f33"/></svg>
  <svg class="icon" style="left:296px;top:557px" width="46" height="46" viewBox="0 0 46 46" aria-hidden="true"><circle cx="23" cy="23" r="21" fill="none" stroke="#233f33" stroke-width="1"/><path d="M23 2 A21 21 0 0 1 44 23" fill="none" stroke="#233f33" stroke-width="2"/><ellipse cx="23" cy="24" rx="5" ry="7" fill="none" stroke="#233f33"/></svg>
  <svg class="icon" style="left:389px;top:557px" width="46" height="46" viewBox="0 0 46 46" aria-hidden="true"><circle cx="23" cy="23" r="21" fill="none" stroke="#233f33" stroke-width="1"/><path d="M23 2 A21 21 0 0 1 44 23" fill="none" stroke="#233f33" stroke-width="2"/><path d="M23 32 V16 M23 24 Q17 22 16 17 Q22 18 23 24 M23 21 Q29 19 30 14 Q24 15 23 21" fill="none" stroke="#233f33"/><path d="M15 32 H31" stroke="#233f33"/></svg>

  <div class="abs label center" style="left:86px;top:612px;width:92px;font-size:7.5px">Seeding</div>
  <div class="abs label center" style="left:179px;top:612px;width:92px;font-size:7.5px">Waterings</div>
  <div class="abs label center" style="left:273px;top:612px;width:92px;font-size:7.5px">Wait a plant</div>
  <div class="abs label center" style="left:366px;top:612px;width:92px;font-size:7.5px">Grow</div>
  <p class="abs body-dark center" style="left:84px;top:632px;width:96px;font-size:4.6px">Lorem ipsum dolor sit amet, consectetur adipiscing elit, sed do eiusmod tempor incididunt.</p>
  <p class="abs body-dark center" style="left:177px;top:632px;width:96px;font-size:4.6px">Lorem ipsum dolor sit amet, consectetur adipiscing elit, sed do eiusmod tempor incididunt.</p>
  <p class="abs body-dark center" style="left:271px;top:632px;width:96px;font-size:4.6px">Lorem ipsum dolor sit amet, consectetur adipiscing elit, sed do eiusmod tempor incididunt.</p>
  <p class="abs body-dark center" style="left:364px;top:632px;width:96px;font-size:4.6px">Lorem ipsum dolor sit amet, consectetur adipiscing elit, sed do eiusmod tempor incididunt.</p>
  <div class="btn btn-forest" style="left:242px;top:678px;width:60px;height:16px;font-size:5px">Contact us →</div>

  <div class="video-card" style="left:91px;top:726px;width:188px;height:142px"></div>
  <div class="abs video-title" style="left:114px;top:750px;font-size:15px">How we produce<br><b>Seebombs</b></div>
  <p class="abs body-light" style="left:114px;top:800px;width:110px;font-size:5.5px">Lorem Ipsum is simply dummy text of the printing and typesetting industry lorem Ipsum has been the industry's standard dummy text ever since.</p>
  <div class="photo ph-field" role="img" aria-label="Video still: two clients planting a seedling in the field" style="left:279px;top:726px;width:175px;height:142px"></div>
  <svg class="icon" style="left:354px;top:790px" width="16" height="16" viewBox="0 0 16 16" aria-hidden="true"><circle cx="8" cy="8" r="7" fill="none" stroke="#fff"/><path d="M6.5 5 L11 8 L6.5 11Z" fill="#fff"/></svg>

  <div class="abs center" style="left:0;top:904px;width:546px;font-family:var(--serif);font-size:12px;color:var(--forest)"><span style="display:inline-block;width:9px;height:9px;border:1.4px solid var(--forest);border-radius:2px;margin-right:4px;vertical-align:-1px"></span>BRENZELGUT</div>
  <div class="photo ph-a" role="img" aria-label="Instagram photo: client with yellow flowers" style="left:91px;top:933px;width:87px;height:87px"></div>
  <div class="photo ph-b" role="img" aria-label="Instagram photo: client holding a seedbomb box" style="left:183px;top:933px;width:87px;height:87px"></div>
  <div class="photo ph-c" role="img" aria-label="Instagram photo: dark clay sculptures" style="left:275px;top:933px;width:87px;height:87px"></div>
  <div class="photo ph-d" role="img" aria-label="Instagram photo: garden installation with autumn tree" style="left:367px;top:933px;width:87px;height:87px"></div>
  <div class="photo ph-e" role="img" aria-label="Instagram photo: clients in front of the house garden" style="left:91px;top:1025px;width:87px;height:87px"></div>
  <div class="photo ph-f" role="img" aria-label="Instagram photo: client at a table in the garden" style="left:183px;top:1025px;width:87px;height:87px"></div>
  <div class="photo ph-g" role="img" aria-label="Instagram photo: framed painting" style="left:275px;top:1025px;width:87px;height:87px"></div>
  <div class="photo ph-h" role="img" aria-label="Instagram photo: two clients reading together" style="left:367px;top:1025px;width:87px;height:87px"></div>
  <div class="btn btn-outline" style="left:230px;top:1135px;width:86px;height:16px;font-size:5px">Follow us on instagram →</div>

  <div class="band" style="top:1198px;height:253px;background:var(--forest);z-index:0"></div>
  <div class="band blush" style="top:1150px;height:113px;border-bottom-right-radius:50px"></div>
  <div class="newsletter" style="left:48px;top:1202px;width:449px;height:117px;border-top-left-radius:44px"></div>
  <div class="abs h2 center" style="left:0;top:1188px;width:546px;font-size:16px">Subscribe to our <b>newsletter</b></div>
  <p class="abs body-dark center" style="left:0;top:1212px;width:546px;font-size:5.5px">Would you like to stay up to date on what's happening in the Brenzelgut?<br>Then subscribe to our newsletter:</p>
  <div class="abs placeholder" style="left:139px;top:1270px;font-size:5.5px">Enter your email address</div>
  <div class="input-line" style="left:135px;top:1282px;width:224px"></div>
  <div class="btn btn-outline" style="left:361px;top:1268px;width:51px;height:15px;font-size:4.5px">Subscribe →</div>

  <div class="abs logo-text" style="left:91px;top:1341px;font-size:16px">BRENZELGUT</div>
  <div class="abs footer-text" style="left:91px;top:1368px;font-size:4.5px">© 2023 <b>Brenzelgut</b>. All Rights Reserved.</div>
  <div class="abs footer-head" style="left:234px;top:1342px;font-size:7.5px">Contact us</div>
  <div class="abs footer-text" style="left:234px;top:1361px;font-size:5.5px">☏&nbsp; 0041 61 555 02 48</div>
  <div class="abs footer-text" style="left:234px;top:1376px;font-size:4.5px">✉&nbsp; info@brenzelgut.ch</div>
  <div class="abs footer-text" style="left:234px;top:1390px;font-size:4.5px">⌖&nbsp; Brenzelgut<br>&nbsp;&nbsp;&nbsp;&nbsp;Lindenweg 14<br>&nbsp;&nbsp;&nbsp;&nbsp;4410 Liestal</div>
  <div class="abs footer-head" style="left:337px;top:1342px;font-size:7.5px">Office hours</div>
  <div class="abs footer-text" style="left:337px;top:1361px;font-size:4.5px">Monday - Friday<br>09:00 to 12:00 &amp; 13:00 to 17:00</div>
  <div class="btn btn-sage" style="left:337px;top:1393px;width:57px;height:15px;font-size:4.5px">Spende jetzt →</div>
  <div class="social" style="left:441px;top:1347px;width:12px;height:12px"></div>
  <div class="social" style="left:441px;top:1364px;width:12px;height:12px"></div>
</section>

<!-- Mobile layout -->
<section class="page mobile" aria-label="Mobile landing page">
  <div class="band blush" style="top:1500px;height:730px"></div>
  <div class="band sage" style="top:371px;height:1200px;border-bottom-left-radius:32px"></div>
  <div class="band hero" style="height:371px"></div>

  <div class="abs logo-text" style="left:8px;top:8px;font-size:11px">BRENZELGUT</div>
  <div class="badge" style="left:139px;top:0;width:37px;height:37px"></div>
  <div class="abs eyebrow center" style="left:0;top:59px;width:176px">Welcome to</div>
  <div class="abs h1 center" style="left:0;top:70px;width:176px;font-size:19px">Brenzelgut</div>
  <p class="abs body-light center" style="left:8px;top:102px;width:168px;font-size:5.6px;line-height:2">A differentiated range of day activities and an individually adapted care setting are aimed at adults of all ages with a mental disability and with physical and psychological impairments.</p>
  <div class="btn btn-sage" style="left:36px;top:169px;width:111px;height:20px;font-size:6.5px">Explore seedbombs →</div>
  <div class="photo ph-workshop" role="img" aria-label="Photo of two clients working on wooden crafts in the workshop" style="left:8px;top:224px;width:168px;height:147px;border-top-left-radius:22px"></div>
  <div class="photo ph-workshop" role="img" aria-label="Small workshop detail photo" style="left:8px;top:371px;width:34px;height:27px"></div>

  <div class="abs" style="left:25px;top:424px;font-family:var(--serif);font-size:6px;color:var(--forest)">Love ♥ Gardening?</div>
  <div class="abs h2" style="left:25px;top:433px;font-size:14px;font-weight:600">Seedbombs kit</div>
  <p class="abs body-dark" style="left:25px;top:452px;width:140px;font-size:6px;line-height:2">A differentiated range of day activities and an individually adapted care setting are aimed at adults ...</p>
  <div class="abs" style="left:25px;top:501px;font-family:var(--serif);font-size:8px;color:var(--forest)">$199.00</div>
  <div class="btn btn-forest" style="left:25px;top:520px;width:112px;height:21px;font-size:6.5px">Explore seedbombs →</div>
  <div class="btn btn-outline" style="left:25px;top:546px;width:77px;height:15px;font-size:6px">Add to cart →</div>
  <div class="photo ph-box" role="img" aria-label="Photo of the green seedbomb package" style="left:0;top:584px;width:87px;height:90px;border-top-left-radius:14px"></div>
  <div class="photo ph-tools" role="img" aria-label="Photo of seed trays, soil and garden tools" style="left:97px;top:629px;width:79px;height:90px;border-top-left-radius:14px"></div>

  <div class="abs h2 center" style="left:0;top:750px;width:176px;font-size:13px">Manual how to use the<br><b>seedbombs</b></div>

  <svg class="icon" style="left:52px;top:803px" width="72" height="72" viewBox="0 0 72 72" aria-hidden="true"><circle cx="36" cy="36" r="34" fill="none" stroke="#233f33" stroke-width="1.4"/><path d="M36 2 A34 34 0 0 1 70 36" fill="none" stroke="#233f33" stroke-width="2.6"/><circle cx="36" cy="33" r="6" fill="none" stroke="#233f33" stroke-width="1.4"/><path d="M24 47 Q36 41 48 47" fill="none" stroke="#233f33" stroke-width="1.4"/></svg>
  <svg class="icon" style="left:52px;top:945px" width="72" height="72" viewBox="0 0 72 72" aria-hidden="true"><circle cx="36" cy="36" r="34" fill="none" stroke="#233f33" stroke-width="1.4"/><path d="M36 2 A34 34 0 0 1 70 36" fill="none" stroke="#233f33" stroke-width="2.6"/><path d="M36 24 Q45 36 36 46 Q27 36 36 24Z" fill="none" stroke="#233f33" stroke-width="1.4"/></svg>
  <svg class="icon" style="left:52px;top:1087px" width="72" height="72" viewBox="0 0 72 72" aria-hidden="true"><circle cx="36" cy="36" r="34" fill="none" stroke="#233f33" stroke-width="1.4"/><path d="M36 2 A34 34 0 0 1 70 36" fill="none" stroke="#233f33" stroke-width="2.6"/><ellipse cx="36" cy="37" rx="8" ry="11" fill="none" stroke="#233f33" stroke-width="1.4"/></svg>
  <svg class="icon" style="left:52px;top:1228px" width="72" height="72" viewBox="0 0 72 72" aria-hidden="true"><circle cx="36" cy="36" r="34" fill="none" stroke="#233f33" stroke-width="1.4"/><path d="M36 2 A34 34 0 0 1 70 36" fill="none" stroke="#233f33" stroke-width="2.6"/><path d="M36 50 V24 M36 38 Q27 35 25 27 Q34 29 36 38 M36 33 Q45 30 47 22 Q38 24 36 33" fill="none" stroke="#233f33" stroke-width="1.4"/><path d="M24 50 H48" stroke="#233f33" stroke-width="1.4"/></svg>

  <div class="abs label center" style="left:0;top:884px;width:176px;font-size:8.5px">Seeding</div>
  <p class="abs body-dark center" style="left:10px;top:903px;width:156px;font-size:5.4px">Lorem ipsum dolor sit amet, consectetur adipiscing elit, sed do eiusmod tempor incididunt.</p>
  <div class="abs label center" style="left:0;top:1026px;width:176px;font-size:8.5px">Waterings</div>
  <p class="abs body-dark center" style="left:10px;top:1045px;width:156px;font-size:5.4px">Lorem ipsum dolor sit amet, consectetur adipiscing elit, sed do eiusmod tempor incididunt.</p>
  <div class="abs label center" style="left:0;top:1167px;width:176px;font-size:8.5px">Wait a plant</div>
  <p class="abs body-dark center" style="left:10px;top:1186px;width:156px;font-size:5.4px">Lorem ipsum dolor sit amet, consectetur adipiscing elit, sed do eiusmod tempor incididunt.</p>
  <div class="abs label center" style="left:0;top:1309px;width:176px;font-size:8.5px">Grow</div>
  <p class="abs body-dark center" style="left:10px;top:1328px;width:156px;font-size:5.4px">Lorem ipsum dolor sit amet, consectetur adipiscing elit, sed do eiusmod tempor incididunt.</p>
  <div class="btn btn-forest" style="left:47px;top:1374px;width:89px;height:20px;font-size:6.5px">Contact us →</div>

  <div class="video-card" style="left:8px;top:1428px;width:168px;height:143px;border-top-left-radius:4px"></div>
  <div class="abs video-title center" style="left:8px;top:1444px;width:168px;font-size:13px">How we produce<br><b>Seebombs</b></div>
  <p class="abs body-light center" style="left:16px;top:1500px;width:152px;font-size:5.8px;line-height:2">Lorem Ipsum is simply dummy text of the printing and typesetting industry lorem Ipsum has been the industry's standard dummy text ever since.</p>
  <div class="photo ph-field" role="img" aria-label="Video still: two clients planting a seedling in the field" style="left:8px;top:1571px;width:168px;height:135px"></div>

  <div class="abs center" style="left:0;top:1739px;width:176px;font-family:var(--serif);font-size:12.5px;color:var(--forest)"><span style="display:inline-block;width:10px;height:10px;border:1.5px solid var(--forest);border-radius:2px;margin-right:4px;vertical-align:-1px"></span>BRENZELGUT</div>
  <div class="photo ph-a" role="img" aria-label="Instagram photo: client with yellow flowers" style="left:8px;top:1775px;width:81px;height:81px"></div>
  <div class="photo ph-b" role="img" aria-label="Instagram photo: client holding a seedbomb box" style="left:95px;top:1775px;width:81px;height:81px"></div>
  <div class="photo ph-c" role="img" aria-label="Instagram photo: dark clay sculptures" style="left:8px;top:1860px;width:81px;height:81px"></div>
  <div class="photo ph-d" role="img" aria-label="Instagram photo: garden installation with autumn tree" style="left:95px;top:1860px;width:81px;height:81px"></div>
  <div class="photo ph-e" role="img" aria-label="Instagram photo: clients in front of the house garden" style="left:8px;top:1945px;width:81px;height:81px"></div>
  <div class="photo ph-f" role="img" aria-label="Instagram photo: client at a table in the garden" style="left:95px;top:1945px;width:81px;height:81px"></div>
  <div class="btn btn-outline" style="left:28px;top:2050px;width:127px;height:19px;font-size:6.5px">Follow us on instagram →</div>

  <div class="band" style="top:2150px;height:506px;background:var(--forest)"></div>
  <div class="band blush" style="top:2100px;height:96px;border-bottom-right-radius:26px"></div>
  <div class="newsletter" style="left:8px;top:2112px;width:159px;height:166px;border-top-left-radius:28px"></div>
  <div class="abs h2 center" style="left:0;top:2100px;width:176px;font-size:13px">Subscribe to our<br><b>newsletter</b></div>
  <p class="abs body-dark center" style="left:14px;top:2136px;width:148px;font-size:5.8px;line-height:2">Would you like to stay up to date on what's happening in the Brenzelgut? Then subscribe to our newsletter:</p>
  <div class="abs placeholder center" style="left:8px;top:2197px;width:159px;font-size:6.5px">Enter your email address</div>
  <div class="input-line" style="left:17px;top:2210px;width:142px"></div>
  <div class="btn btn-outline" style="left:37px;top:2212px;width:78px;height:19px;font-size:6.5px">Subscribe →</div>

  <div class="abs logo-text" style="left:8px;top:2303px;font-size:17px">BRENZELGUT</div>
  <div class="abs footer-head" style="left:8px;top:2349px;font-size:10px">Contact us</div>
  <div class="abs footer-text" style="left:8px;top:2377px;font-size:6.5px">☏&nbsp;&nbsp; 0041 61 555 02 48</div>
  <div class="abs footer-text" style="left:8px;top:2398px;font-size:6.5px">✉&nbsp;&nbsp; info@brenzelgut.ch</div>
  <div class="abs footer-text" style="left:8px;top:2418px;font-size:6.2px">⌖&nbsp;&nbsp; Brenzelgut<br>&nbsp;&nbsp;&nbsp;&nbsp;&nbsp;&nbsp;Lindenweg 14<br>&nbsp;&nbsp;&nbsp;&nbsp;&nbsp;&nbsp;4410 Liestal</div>
  <div class="abs footer-head" style="left:8px;top:2478px;font-size:10px">Office hours</div>
  <div class="abs footer-text" style="left:8px;top:2502px;font-size:6.5px">Monday - Friday<br>09:00 to 12:00 &amp; 13:00 to 17:00</div>
  <div class="btn btn-sage" style="left:8px;top:2540px;width:86px;height:20px;font-size:6.5px">Spende jetzt →</div>
  <div class="rule" style="left:0;top:2579px;width:176px"></div>
  <div class="social" style="left:78px;top:2592px;width:18px;height:18px"></div>
  <div class="social" style="left:104px;top:2592px;width:18px;height:18px"></div>
  <div class="abs footer-text center" style="left:0;top:2627px;width:176px;font-size:6px">© 2023 <b>Brenzelgut</b>. All Rights Reserved.</div>
</section>

</body>
</html>
```